User-interface and web design for new forum-style communication platform

We developed a new forum-style communication platform specially targetting Ticker Circle to share and discuss information on companies listed on the stock exchange.

You have complete freedom for designing the user-interface and web design. Designs should include all features listed below.

Please read the attached document for full specifications. Also attached is a mockup of the layout, but this is only directional. A mockup for the user-profile is also attached, but does not need to be designed.

This project focusses on the homepage and thread view.

The winner(s) will be asked to design the complete project. (create thread box, user profile, registering, settings...)

We are looking for a well thought out, smart design that incorporates the specifications in the attached document. Please do not hesitate to contact us if anything is not clear.

Target Market(s)

Ticker Circle from 25 to 60 years old (the people that are currently on investor forums)

Industry/Entity Type

Communication

Font styles to use
Sans Serif

Colors

Designer to choose colors to be used in the design.

Requirements
Must have
• Full homepage design & Thread view specified in the attached document.
Nice to have
• Create thread view
- Field for adding tags
- field for subject of the thread
- text box with basic text editing
- method for sharing media
Should not have
• Logo design.

```html
<!DOCTYPE html>
<html lang="en">
<head>
<meta charset="utf-8">
<title>Ticker Circle – Public threads</title>
<link href="https://fonts.googleapis.com/css2?family=Nunito+Sans:wght@400;600;800&display=swap" rel="stylesheet">
<style>
:root{
  --bg:#e8e8e8;
  --panel:#444444;
  --panel-dark:#3a3a3a;
  --blue:#00a8f0;
  --blue-deep:#0a6cf0;
  --lime:#dcef00;
  --text:#444;
  --muted:#8a8a8a;
  --white:#fff;
  --line:#d6d6d6;
  --footer:#2c2c2c;
}
*{box-sizing:border-box;margin:0;padding:0}
html,body{width:1200px;height:1044px;overflow:hidden;background:var(--bg);font-family:"Nunito Sans",Arial,sans-serif;color:var(--text)}
.canvas{position:relative;width:1200px;height:1044px}
.abs{position:absolute}
/* sidebar */
.sidebar{left:151px;top:0;width:219px;height:976px;background:var(--panel)}
.brand{left:20px;top:30px;color:var(--white);font-weight:800;font-size:23px;letter-spacing:.5px}
.brand-rule{left:20px;top:62px;width:178px;height:2px;background:var(--white)}
.users{left:0;top:99px;width:219px;height:94px;background:var(--white)}
.users h3{position:absolute;left:21px;top:14px;font-weight:400;font-size:16px;color:#555}
.field{background:var(--white);border:1px solid var(--line);border-radius:2px;display:flex;align-items:center;color:#999;font-size:11px}
.field span{flex:1;padding-left:12px}
.field .icon{width:28px;height:100%;border-left:1px solid var(--line);display:flex;align-items:center;justify-content:center}
.band{left:0;width:219px;height:42px;background:var(--blue);color:var(--white);font-size:16px;padding:12px 0 0 22px;text-shadow:0 1px 1px rgba(0,0,0,.25)}
.chip{height:23px;border:1px solid #bbb;color:var(--white);font-size:10.5px;padding:3px 0 0 7px;border-radius:2px}
.btn{display:flex;align-items:center;justify-content:center;font-size:13px;border-radius:2px}
.btn.lime{background:var(--lime);color:#444}
.btn.blue{background:var(--blue);color:var(--white)}
.btn.deep{background:var(--blue-deep);color:var(--white)}
.btn.dark{background:var(--panel);color:var(--white)}
.tag{height:24px;background:var(--lime);color:#555;font-size:10px;display:flex;align-items:center;justify-content:center}
.peek{left:94px;top:531px;width:175px;height:112px;background:var(--lime);font-size:9.5px;color:#666}
.contrib{left:21px;width:175px;height:22px;color:var(--white);font-size:10px;border-bottom:1px solid #5a5a5a;padding-top:5px}
.count{position:absolute;width:16px;height:16px;border-radius:50%;background:var(--blue);color:var(--white);font-size:7px;display:flex;align-items:center;justify-content:center;border:1px solid var(--white)}
/* main */
.crumbs{left:409px;top:80px;font-size:12px;color:#555;display:flex;gap:13px}
.crumbs .active{color:var(--blue-deep)}
.badge{left:914px;top:34px;width:27px;height:27px;border-radius:50%;background:#fbf57a;font-size:15px;display:flex;align-items:center;justify-content:center;color:#333}
.tabs{left:409px;top:127px;width:266px;height:41px;background:var(--white);border:1px solid var(--line);border-bottom:none;display:flex;font-size:16px}
.tabs div{padding:11px 0 0 12px;height:100%}
.tabs .on{background:var(--panel);color:var(--white);width:71px}
.card{left:409px;width:642px;height:221px;background:var(--white);border:1px solid var(--line)}
.photo{position:absolute;left:14px;width:131px;height:123px;border-radius:2px}
.title{position:absolute;left:169px;font-size:16px;color:#444}
.meta{position:absolute;left:169px;font-size:11px;color:#333}
.meta b,.link{color:var(--blue-deep);font-weight:400}
.body{position:absolute;left:169px;width:430px;font-size:11.6px;line-height:15.8px;color:var(--muted)}
.stats{position:absolute;left:169px;font-size:12px;color:#333}
.actions{position:absolute;right:14px;display:flex;gap:4px}
.dropdown{left:410px;top:167px;width:128px;background:var(--panel);color:var(--white);font-size:15px;border-radius:0 0 3px 3px;z-index:2}
.dropdown div{height:30px;padding:5px 0 0 13px;border-top:1px solid #555}
.avatar{left:423px;width:77px;height:71px;border:1px solid var(--line)}
.reply{left:525px;width:525px;height:72px;background:var(--white);border:1px solid var(--line);font-size:10.6px;color:#666}
.reply p{padding:7px 15px;line-height:15.5px;border-bottom:1px dotted #ccc;height:43px}
.stranger{position:absolute;right:0;bottom:0;width:115px;height:30px}
.footer{left:0;top:976px;width:1200px;height:46px;background:var(--footer);color:var(--white);font-size:11px;display:flex;align-items:center;justify-content:center}
</style>
</head>
<body>
<div class="canvas">

  <aside class="abs sidebar">
    <div class="abs brand">TICKER CIRCLE</div>
    <div class="abs brand-rule"></div>

    <div class="abs users">
      <h3>Users</h3>
      <div class="abs field" style="left:21px;top:41px;width:176px;height:29px"><span>Search...</span><div class="icon"><svg width="11" height="11" viewBox="0 0 12 12"><circle cx="5" cy="5" r="3.8" fill="none" stroke="#aaa" stroke-width="1.5"/><path d="M8 8l3 3" stroke="#aaa" stroke-width="1.5"/></svg></div></div>
    </div>

    <div class="abs band" style="top:219px">Saved filters</div>
    <div class="abs chip" style="left:21px;top:278px;width:131px">★ Lorem Ipsum</div>
    <div class="abs chip" style="left:21px;top:305px;width:149px">★ Printing and typ Setting</div>
    <div class="abs chip" style="left:21px;top:333px;width:137px">★ Ind Ipsum has Ft Been</div>
    <div class="abs chip" style="left:21px;top:360px;width:129px">★ Endustry's Standard</div>
    <div class="abs btn lime" style="left:22px;top:395px;width:72px;height:25px">Show all</div>

    <div class="abs band" style="top:440px">Popular Tags</div>
    <div class="abs tag" style="left:23px;top:503px;width:58px">DUMMY</div>
    <div class="abs tag" style="left:85px;top:503px;width:56px">HAS</div>
    <div class="abs tag" style="left:139px;top:503px;width:58px">LETRAS</div>
    <div class="abs tag" style="left:22px;top:532px;width:68px">UNKNOW</div>
    <div class="abs peek">
      <div style="position:absolute;left:9px;top:8px;font-size:10px">DUMMY</div>
      <div style="position:absolute;left:9px;top:24px">Lorem Ipsum is</div>
      <div style="position:absolute;left:9px;top:39px;background:var(--blue);color:#fff;padding:2px 3px;width:77px">simply dummy</div>
      <div style="position:absolute;left:9px;top:60px;width:77px;border-bottom:1px solid #bcc900;padding-bottom:3px">text of the print-</div>
      <div style="position:absolute;left:9px;top:80px">ing and typeset-</div>
      <div role="img" aria-label="Photo of traders outside an exchange" style="position:absolute;left:92px;top:24px;width:72px;height:68px;background:linear-gradient(160deg,#2b4d8a,#8a93a6 60%,#3a3a42)"></div>
    </div>
    <div class="abs tag" style="left:22px;top:648px;width:59px">IPSUM</div>
    <div class="abs tag" style="left:84px;top:648px;width:59px">GALEY</div>
    <div class="abs btn blue" style="left:22px;top:691px;width:72px;height:23px">Show all</div>

    <div class="abs band" style="top:734px">Popular Contributors</div>
    <div class="abs contrib" style="top:792px">★&nbsp; Lorem Ipsum is<span class="count" style="left:88px;top:-2px">25</span></div>
    <div class="abs contrib" style="top:814px">★&nbsp; dummy text of the printi<span class="count" style="left:128px;top:-4px">35</span></div>
    <div class="abs contrib" style="top:836px">★&nbsp; typesetting industry.<span class="count" style="left:108px;top:-4px">38</span></div>
    <div class="abs contrib" style="top:858px;border:none">★&nbsp; Lorem Ipsum has been<span class="count" style="left:124px;top:-4px">49</span></div>
    <div class="abs btn blue" style="left:22px;top:895px;width:72px;height:23px">Show all</div>
  </aside>

  <!-- top bar -->
  <div class="abs field" style="left:409px;top:30px;width:263px;height:37px;font-size:12px"><span style="padding-left:16px">#northwind#brightlane</span><div class="icon" style="width:44px"><svg width="15" height="15" viewBox="0 0 12 12"><circle cx="5" cy="5" r="3.8" fill="none" stroke="#aaa" stroke-width="1.4"/><path d="M8 8l3 3" stroke="#aaa" stroke-width="1.4"/></svg></div></div>
  <div class="abs btn blue" style="left:676px;top:30px;width:73px;height:37px;font-size:14px">SAVE</div>
  <div class="abs btn dark" style="left:752px;top:30px;width:72px;height:37px;font-size:14px">CLEAR</div>
  <div class="abs badge">3</div>
  <div class="abs" style="left:893px;top:64px;font-size:9.5px;color:#444">1 New follower</div>
  <div class="abs btn blue" style="left:968px;top:30px;width:80px;height:37px;font-size:17px;justify-content:flex-start;padding-left:11px">User
    <svg style="position:absolute;right:12px;top:16px" width="9" height="5" viewBox="0 0 9 5"><path d="M0 0h9L4.5 5z" fill="#fff"/></svg></div>

  <nav class="abs crumbs"><span>Home</span><span>Conversotions</span><span>Public</span><span class="active">#northwind#brightlane</span></nav>

  <div class="abs tabs"><div class="on">Public</div><div style="width:96px;border-right:1px solid #e4e4e4">Following</div><div>Contacts</div></div>
  <div class="abs dropdown"><div>Lorem Ipsum</div><div>Lorem Ipsum</div></div>

  <!-- post 1 -->
  <article class="abs card" style="top:167px">
    <div class="photo" role="img" aria-label="Photo of a trader on the exchange floor" style="top:65px;background:linear-gradient(150deg,#3c3f52,#7a6a66 45%,#1f2a48)"></div>
    <div class="title" style="top:22px">Lorem Ipsum has been industry's</div>
    <div class="meta" style="top:48px">Posted on <b>Mar 01, 2014</b> by admin</div>
    <p class="body" style="top:73px">Lorem Ipsum is simply dummy text of the printing and typesetting industry. Lorem Ipsum has been the industry's standard dummy text ever since the 1500s. when an unknown printer took a galley of type and scrambled it to make a type speci-men book. It has survived not only five centuries, but also the leap into electronic typesetting, remaining essentially unchanged. It was popularised in the 1960s with the release of Typeline sheets containing..</p>
    <div class="stats" style="top:200px">12 <span class="link">replies</span>&nbsp; 250 <span class="link">views</span> &nbsp;&nbsp;&nbsp;&nbsp; <span class="link">Read More</span> ›</div>
    <div class="actions" style="top:196px"><div class="btn deep" style="width:57px;height:26px">Reply</div><div class="btn dark" style="width:57px;height:26px">Share</div><div class="btn lime" style="width:83px;height:26px">Favourite</div></div>
  </article>

  <div class="abs avatar" role="img" aria-label="Member avatar photo" style="top:423px;background:linear-gradient(160deg,#9aa48a,#6b6a4a 55%,#4d5a3a)"></div>
  <div class="abs reply" style="top:423px"><p>Lorem Ipsum is simply dummy text of the printing and typesetting industry.<br>Lorem Ipsum has been the industry's ..</p><div class="stranger btn blue">Post as Stranger</div></div>

  <!-- post 2 -->
  <article class="abs card" style="top:529px">
    <div class="photo" role="img" aria-label="Photo of a speaker in a suit" style="top:27px;background:linear-gradient(150deg,#e6e8f5,#b9bbcf 50%,#3a3a44)"></div>
    <div class="abs" style="left:14px;top:166px;width:131px;height:34px;border:1px solid var(--line);font-size:15px;padding:6px 0 0 15px;background:#fff">View all posts</div>
    <div class="title" style="top:22px">Lorem Ipsum has been industry's</div>
    <div class="meta" style="top:48px">Posted on <b>Mar 01, 2014</b> by admin</div>
    <p class="body" style="top:73px">Lorem Ipsum is simply dummy text of the printing and typesetting industry. Lorem Ipsum has been the industry's standard dummy text ever since the 1500s. when an unknown printer took a galley of type and scrambled it to make a type speci-men book. It has survived not only five centuries, but also the leap into electronic typesetting, remaining essentially unchanged. It was popularised in the 1960s with the release of Typeline sheets containing..</p>
    <div class="stats" style="top:200px">12 <span class="link">replies</span>&nbsp; 250 <span class="link">views</span> &nbsp;&nbsp;&nbsp;&nbsp; <span class="link">Read More</span> ›</div>
    <div class="actions" style="top:196px"><div class="btn deep" style="width:57px;height:26px">Reply</div><div class="btn dark" style="width:57px;height:26px">Share</div><div class="btn lime" style="width:83px;height:26px">Favourite</div></div>
  </article>

  <div class="abs avatar" role="img" aria-label="Member avatar photo" style="top:784px;background:linear-gradient(160deg,#2c3f6e,#5f6f9a 55%,#1c2233)"></div>
  <div class="abs reply" style="top:784px"><p>Lorem Ipsum is simply dummy text of the printing and typesetting industry.<br>Lorem Ipsum has been the industry's ..</p><div class="stranger btn blue">Post as Stranger</div></div>

  <footer class="abs footer">Copyright © 2014 tickercircle.com</footer>
</div>
</body>
</html>
```